Vesta Power Web Design

I want a design for a home page that can function as a template for the entire web design. I"m also requesting that the design be adapted as a template for Power Point presentations, as well.

Here"s a brief about our company:

Vesta Power provides its customers with clean, redundant and reliable power. Functioning as a private power producer, Vesta Power owns and operates combined heat and power (CHP) and distributed generation (DG) systems.

Vesta’s management has extensive experience in aerospace turbines engine operation, maintenance, manufacturing and repair. Depending on the customer need, Vesta either builds new generators or refurbish “retired” aerospace turbines into industrial generators. This allows Vesta to deliver generating systems at greatly reduced capital outlays, enabling Vesta Power to offer its customers not only redundant power and grid independence, but significant savings on their energy needs. Vesta’s typical installation size is 500Kws to 3Mws but based upon our customer"s needs, Vesta can site multiple generators to configure systems of larger size.

By using aero derivative turbine engines the company has the flexibility to use the best source of fuel for each site and power requirement. The turbine engine can operate on virtually any combustible fuel. This allows Vesta to utilize the flex fuel practice and operate on either the least expensive fuel available or operate on renewable and biofuels to fulfill the green power requirements mandated by many federal, state and local utility commissions.

Vesta’s market strategy is as follows:

1. Sell reliable and redundant power through a PPAs or lease agreements to industrial or institutional customers with high electrical and thermal needs such as food processors, bio fuel producers, hospitals, casinos, hotels, etc.

2. Lease its systems to customer that “flare gas” as byproducts of their processes such as wastewater treatment facilities, land fills and "stranded gas wells" allowing them to use their waste products to power their facilities and sell excess electricity back to the grid.

3. Partner with other private power producers to provide the turbine generating capacity on a leased basis.
Updates

Please disregard the "turbine logo" that was uploaded as a file and focus only on the "bolt design logo", A (bolt) E.

We like the simple navigation and clean and modern design of sites.

http://www.plumvault.example/

http://www.serviqo.example/

http://www.trylumo.example/

Target Market(s)

Our target markets can be found on the web architecture file I've attached to this submission.

Number of Pages Required

1 page

Requirements
Must have
• The designer must provide a web design and a Power Point template based upon the web design.

• The design must contemplate the web architecture that I""ve included as a file.

```html
<!DOCTYPE html>
<html lang="en">
<head>
<meta charset="utf-8">
<title>Vesta Power – Web &amp; Slide Template</title>
<link href="https://fonts.googleapis.com/css2?family=Arimo:wght@400;700&display=swap" rel="stylesheet">
<style>
:root{
  --side-green:#a9cdb6;
  --mint-light:#e6f3ea;
  --mint-mid:#bfddca;
  --brand-green:#1e6a1f;
  --frame:#dde4e2;
  --nav-top:#97a6a1;
  --nav-bottom:#6d7d78;
  --nav-text:#f2f6f4;
  --sub-top:#d6eadd;
  --sub-bottom:#b3d2be;
  --sub-active:#9fd3ad;
  --sub-text:#4d5a55;
  --btn-top:#6f7887;
  --btn-bottom:#4b5362;
  --btn-text:#cfd4dc;
  --body-text:#1c1c1c;
}
*{box-sizing:border-box;margin:0;padding:0}
html,body{width:1200px;height:2470px;overflow:hidden;background:#fff}
body{position:relative;font-family:"Arimo",Arial,sans-serif}

.page{position:absolute;left:0;width:1200px;height:833px;background:var(--side-green)}
.page--home{top:10px}
.page--menu{top:854px}
.page__column{position:absolute;left:190px;top:0;width:810px;height:100%;
  background:radial-gradient(ellipse 60% 55% at 50% 50%,#f3faf5 0%,var(--mint-light) 35%,var(--mint-mid) 100%)}

.power-mark{position:absolute;border-radius:50%;
  background:radial-gradient(circle,rgba(255,255,255,.55) 0%,rgba(255,255,255,.25) 45%,rgba(255,255,255,.08) 70%,rgba(255,255,255,0) 72%)}
.page .power-mark{left:383px;top:192px;width:500px;height:500px}

.brand{position:absolute;display:flex;align-items:center;gap:8px}
.brand__square{width:40px;height:40px;background:var(--brand-green);box-shadow:0 0 22px 10px rgba(255,255,255,.8)}
.brand__name{font-size:17px;font-weight:700;color:var(--brand-green);white-space:nowrap}
.page .brand{left:223px;top:45px}

.content-frame{position:absolute;left:318px;top:116px;width:670px;height:628px;
  border:3px solid var(--frame);box-shadow:0 0 2px rgba(80,100,95,.35)}

.main-nav{position:absolute;left:202px;top:134px;width:160px}
.main-nav__item{position:absolute;left:0;width:140px;height:29px;padding-right:5px;
  background:linear-gradient(var(--nav-top),var(--nav-bottom));
  color:var(--nav-text);font-size:15px;letter-spacing:-.1px;line-height:29px;text-align:right;white-space:nowrap;
  box-shadow:1px 2px 3px rgba(0,0,0,.3)}
.main-nav__item--active{left:-5px;width:155px;padding-right:18px;
  clip-path:polygon(0 0,145px 0,155px 50%,145px 100%,0 100%)}

.body-copy{position:absolute;left:358px;top:153px;width:352px;font-size:10px;line-height:20px;color:var(--body-text);text-align:justify}
.body-copy p{text-indent:12px;margin-bottom:20px}

.feature-photo{position:absolute;left:729px;top:151px;width:220px;height:248px;border:1px solid #2f3a35;
  background:linear-gradient(160deg,#7d93a4 0%,#4b5a52 35%,#6b5a3a 60%,#d9a64a 72%,#3a3b2c 100%)}

.cta{position:absolute;top:719px;width:139px;height:46px;display:flex;align-items:center;justify-content:center;
  background:linear-gradient(var(--btn-top),var(--btn-bottom));border:1px solid #3f4653;
  color:var(--btn-text);font-size:11.5px;line-height:12px;text-align:center;box-shadow:1px 2px 3px rgba(0,0,0,.35)}
.cta--law{left:399px}.cta--fit{left:585px}.cta--calc{left:770px}

.sub-nav__item{position:absolute;height:30px;padding-right:7px;
  background:linear-gradient(var(--sub-top),var(--sub-bottom));color:var(--sub-text);
  border-bottom:1px solid rgba(255,255,255,.7);
  font-size:12px;line-height:29px;text-align:right;white-space:nowrap;
  box-shadow:2px 3px 5px rgba(0,0,0,.3)}
.sub-nav__item--active{background:linear-gradient(#c9eed4,var(--sub-active));padding-right:17px;
  clip-path:polygon(0 0,calc(100% - 10px) 0,100% 50%,calc(100% - 10px) 100%,0 100%)}
.sub-nav__item--tall{height:32px;line-height:12px;padding-top:4px}
.lvl1{left:342px;width:100px}
.lvl2{left:442px;width:84px}
.lvl3{left:526px;width:82px}

.slide{position:absolute;left:92px;top:1701px;width:1016px;height:769px;
  background:radial-gradient(ellipse 55% 55% at 50% 55%,#f5fbf7 0%,var(--mint-light) 35%,var(--mint-mid) 100%)}
.slide .power-mark{left:242px;top:130px;width:520px;height:520px}
.slide__frame{position:absolute;left:68px;top:69px;width:878px;height:636px;border:3px solid var(--frame);box-shadow:0 0 2px rgba(80,100,95,.35)}
.slide .brand{left:28px;top:44px}
</style>
</head>
<body>

<section class="page page--home">
  <div class="page__column"></div>
  <div class="power-mark" role="img" aria-label="Faint glowing power button illustration in the background"></div>
  <div class="brand"><span class="brand__square"></span><span class="brand__name">Vesta Power</span></div>
  <div class="content-frame"></div>
  <nav class="main-nav">
    <div class="main-nav__item" style="top:0">About Vesta</div>
    <div class="main-nav__item main-nav__item--active" style="top:30px">CHP</div>
    <div class="main-nav__item" style="top:61px">Stranded Gas</div>
    <div class="main-nav__item" style="top:91px">Resources</div>
    <div class="main-nav__item" style="top:121px">Partner &amp; Suppliers</div>
    <div class="main-nav__item" style="top:151px">Contact Us</div>
  </nav>
  <div class="body-copy">
    <p>Vesta Power provides its customers with clean, redundant and reliable power. Functioning as a private power producer, Vesta Power owns and operates combined heat and power (CHP) and distributed generation (DG) systems.</p>
    <p>Vesta’s management has extensive experience in aerospace turbines engine operation, maintenance, manufacturing and repair. Depending on the customer need, Vesta either builds new generators or refurbish “retired” aerospace turbines into industrial generators. This allows Vesta to deliver generating systems at greatly reduced capital outlays, enabling Vesta Power to offer its customers not only redundant power and grid independence, but significant savings on their energy needs. Vesta’s typical installation size is 500Kws to 3Mws but based upon our customer"s needs, Vesta can site multiple generators to configure systems of larger size.</p>
    <p>By using aero derivative turbine engines the company has the flexibility to use the best source of fuel for each site and power requirement. The turbine engine can operate on virtually any combustible fuel. This allows Vesta to utilize the flex fuel practice and operate on either the least expensive fuel available or operate on renewable and biofuels to fulfill the green power requirements mandated by many federal, state and local utility commissions.</p>
  </div>
  <div class="feature-photo" role="img" aria-label="Photograph of a glass-walled modern house lit warmly at dusk among trees"></div>
  <a class="cta cta--law">Texas CHP Critical<br>Infrastructure<br>Legislation</a>
  <a class="cta cta--fit">Is your business a good<br>candidate for CHP ?</a>
  <a class="cta cta--calc">CHP Calculator</a>
</section>

<section class="page page--menu">
  <div class="page__column"></div>
  <div class="power-mark" role="img" aria-label="Faint glowing power button illustration in the background"></div>
  <div class="brand"><span class="brand__square"></span><span class="brand__name">Vesta Power</span></div>
  <div class="content-frame"></div>
  <div class="body-copy">
    <p>Vesta Power provides its customers with clean, redundant and reliable power. Functioning as a private power producer, Vesta Power owns and operates combined heat and power (CHP) and distributed generation (DG) systems.</p>
    <p>Vesta’s management has extensive experience in aerospace turbines engine operation, maintenance, manufacturing and repair. Depending on the customer need, Vesta either builds new generators or refurbish “retired” aerospace turbines into industrial generators. This allows Vesta to deliver generating systems at greatly reduced capital outlays, enabling Vesta Power to offer its customers not only redundant power and grid independence, but significant savings on their energy needs. Vesta’s typical installation size is 500Kws to 3Mws but based upon our customer"s needs, Vesta can site multiple generators to configure systems of larger size.</p>
    <p>By using aero derivative turbine engines the company has the flexibility to use the best source of fuel for each site and power requirement. The turbine engine can operate on virtually any combustible fuel. This allows Vesta to utilize the flex fuel practice and operate on either the least expensive fuel available or operate on renewable and biofuels to fulfill the green power requirements mandated by many federal, state and local utility commissions.</p>
  </div>
  <div class="feature-photo" role="img" aria-label="Photograph of a glass-walled modern house lit warmly at dusk among trees"></div>
  <nav class="main-nav">
    <div class="main-nav__item" style="top:0">About Vesta</div>
    <div class="main-nav__item main-nav__item--active" style="top:30px">CHP</div>
    <div class="main-nav__item" style="top:61px">Stranded Gas</div>
    <div class="main-nav__item" style="top:91px">Resources</div>
    <div class="main-nav__item" style="top:121px">Partner &amp; Suppliers</div>
    <div class="main-nav__item" style="top:151px">Contact Us</div>
  </nav>
  <div class="sub-nav">
    <div class="sub-nav__item lvl1 sub-nav__item--active" style="top:164px">What is CHP ?</div>
    <div class="sub-nav__item lvl1" style="top:194px">Benefits</div>
    <div class="sub-nav__item lvl1" style="top:224px">Energy Security</div>
    <div class="sub-nav__item lvl1 sub-nav__item--active" style="top:254px">Markets</div>
    <div class="sub-nav__item lvl2" style="top:254px">Commercial</div>
    <div class="sub-nav__item lvl2 sub-nav__item--active" style="top:284px">Institutional</div>
    <div class="sub-nav__item lvl2" style="top:314px">Industrial</div>
    <div class="sub-nav__item lvl3" style="top:284px">Universities</div>
    <div class="sub-nav__item lvl3" style="top:314px">Hospitals</div>
    <div class="sub-nav__item lvl3 sub-nav__item--tall" style="top:344px">Wastewater<br>Treament</div>
  </div>
  <a class="cta cta--law">Texas CHP Critical<br>Infrastructure<br>Legislation</a>
  <a class="cta cta--fit">Is your business a good<br>candidate for CHP ?</a>
  <a class="cta cta--calc">CHP Calculator</a>
</section>

<section class="slide">
  <div class="power-mark" role="img" aria-label="Soft glowing power button illustration centred on the slide"></div>
  <div class="slide__frame"></div>
  <div class="brand"><span class="brand__square"></span><span class="brand__name">Vesta Power</span></div>
</section>

</body>
</html>
```